Brindle Capital and Investments

Create a simple business card design using the logos attached. Make it similar but not exact to the reference photo. Brand guidelines are also included.

```html
<!DOCTYPE html>
<html lang="en">
<head>
<meta charset="utf-8">
<title>Brindle Capital – Business Card</title>
<link rel="stylesheet" href="https://fonts.googleapis.com/css2?family=Montserrat:wght@400;500;600;700&family=Rye&display=swap">
<style>
  :root {
    --navy: #1f2640;
    --rust: #9e4f22;
    --paper: #ffffff;
    --frame: #8a8a8a;
    --rule: #9a9a9a;
  }
  * { box-sizing: border-box; margin: 0; padding: 0; }
  html, body {
    width: 1033px;
    height: 1200px;
    overflow: hidden;
    background: var(--paper);
  }
  body { position: relative; font-family: "Montserrat", Arial, sans-serif; }

  .card { position: absolute; left: 0; width: 1033px; border: 1px solid var(--frame); }
  .card--front { top: 0; height: 582px; background: var(--navy); }
  .card--back { top: 618px; height: 582px; background: var(--paper); }

  .brand { position: absolute; display: flex; flex-direction: column; align-items: center; }
  .brand__dot { border-radius: 50%; background: var(--rust); }
  .brand__name {
    font-family: "Montserrat", Arial, sans-serif;
    font-weight: 700;
    letter-spacing: 0.16em;
    text-align: center;
    line-height: 1.15;
  }

  .card--front .brand { left: 0; right: 0; top: 140px; }
  .card--front .brand__dot { width: 96px; height: 96px; margin-bottom: 34px; }
  .card--front .brand__name { color: var(--paper); font-size: 40px; }

  .website {
    position: absolute; left: 0; right: 0; top: 480px;
    text-align: center; color: var(--rust);
    font-weight: 500; font-size: 30px; letter-spacing: 0.01em;
  }

  .card--back .brand { left: 96px; width: 360px; top: 170px; }
  .card--back .brand__dot { width: 86px; height: 86px; margin-bottom: 30px; }
  .card--back .brand__name { color: var(--navy); font-size: 34px; }

  .divider { position: absolute; left: 468px; top: 114px; width: 2px; height: 352px; background: var(--rule); }

  .contact { position: absolute; left: 510px; top: 122px; color: var(--navy); }
  .contact__name { font-family: "Rye", Georgia, serif; font-size: 34px; line-height: 1.1; letter-spacing: 0.01em; }
  .contact__title { color: var(--rust); font-weight: 600; font-size: 24px; margin-top: 2px; letter-spacing: 0.02em; }
  .contact__email { color: var(--rust); font-weight: 600; font-size: 28px; margin-top: 62px; }
  .contact__row { display: flex; font-size: 29px; margin-top: 10px; line-height: 1.2; }
  .contact__label { width: 104px; font-weight: 400; }
  .contact__number { color: var(--rust); font-weight: 600; }
  .contact__address { font-size: 29px; line-height: 1.18; margin-top: 10px; font-weight: 400; }
</style>
</head>
<body>
  <section class="card card--front">
    <div class="brand">
      <span class="brand__dot"></span>
      <p class="brand__name">BRINDLE<br>CAPITAL</p>
    </div>
    <p class="website">brindlecapital.com</p>
  </section>

  <section class="card card--back">
    <div class="brand">
      <span class="brand__dot"></span>
      <p class="brand__name">BRINDLE<br>CAPITAL</p>
    </div>
    <div class="divider"></div>
    <div class="contact">
      <h1 class="contact__name">MAREN WHITFIELD</h1>
      <p class="contact__title">MANAGING PARTNER</p>
      <p class="contact__email">maren@brindlecapital.com</p>
      <p class="contact__row"><span class="contact__label">Direct</span><span class="contact__number">713.555.0142</span></p>
      <p class="contact__row"><span class="contact__label">Cell</span><span class="contact__number">713.555.0142</span></p>
      <p class="contact__address">address will come here<br>address will come here</p>
    </div>
  </section>
</body>
</html>
```